Business Card Design

Quorvel Software Limited develops and sells venue and event management software called Quorvel Stagehand, which is available in the cloud or on-premise. The company was established in 1986. Most of our customers are performing arts venues, museums and festivals. Our existing design is a bit dull. We need to convey that we are both innovative and reliable.
Not all our people show their mobile phone numbers on their cards, so the design needs to work land line and mobile or land line only.

Industry/Entity Type

Software

Contact Information for Business Card

Helen Brackwood
Director
Quorvel Software Limited
42B Millbank Lane, Epsom, Surrey, KT19 3DW
Telephone: +44 (0)1372 904213
Mobile: +44 (0)7700 900562
Email: hbrackwood@quorvel.example
Web: www.quorvel.example

```html
<!DOCTYPE html>
<html lang="en">
<head>
<meta charset="utf-8">
<title>Quorvel Software Limited – Business Card</title>
<link rel="stylesheet" href="https://fonts.googleapis.com/css2?family=Open+Sans:ital,wght@0,400;0,600;0,700;1,400&display=swap">
<style>
  :root {
    --backdrop: #e4e5e7;
    --card-white: #ffffff;
    --card-dark: #333435;
    --navy: #123f66;
    --band-blue: #0f4a78;
    --text-blue: #1f66a3;
    --accent-blue: #1d6fa9;
    --white: #ffffff;
  }
  * { margin: 0; padding: 0; box-sizing: border-box; }
  html, body {
    width: 1200px;
    height: 873px;
    overflow: hidden;
    background: var(--backdrop);
    font-family: "Open Sans", Arial, sans-serif;
  }
  .canvas {
    position: relative;
    width: 1200px;
    height: 873px;
  }
  .card {
    position: absolute;
    top: 277px;
    width: 530px;
    height: 318px;
    box-shadow: 0 6px 18px rgba(0, 0, 0, 0.18);
    overflow: hidden;
  }
  .card--front { left: 50px; background: var(--card-white); }
  .card--back  { left: 620px; background: var(--card-dark); }

  /* Front */
  .wordmark {
    position: absolute;
    display: flex;
    align-items: center;
    gap: 10px;
    font-weight: 700;
    letter-spacing: 0.04em;
    text-transform: uppercase;
  }
  .wordmark__square {
    display: block;
    background: var(--accent-blue);
  }
  .card--front .wordmark {
    left: 58px;
    top: 92px;
    font-size: 34px;
    color: var(--navy);
  }
  .card--front .wordmark__square { width: 24px; height: 24px; }

  .contact {
    position: absolute;
    left: 298px;
    top: 150px;
    color: var(--text-blue);
  }
  .contact__name {
    font-size: 17px;
    font-weight: 700;
    color: var(--navy);
    text-transform: uppercase;
    letter-spacing: 0.02em;
    line-height: 1.2;
  }
  .contact__role {
    font-size: 12px;
    font-style: italic;
    margin-bottom: 10px;
  }
  .contact__line {
    font-size: 13px;
    line-height: 1.4;
  }
  .address-band {
    position: absolute;
    left: 0;
    bottom: 0;
    width: 100%;
    height: 34px;
    background: var(--band-blue);
    color: var(--white);
    font-size: 13.5px;
    line-height: 34px;
    padding-left: 18px;
    white-space: nowrap;
  }

  /* Back */
  .card--back .wordmark {
    left: 50%;
    top: 50%;
    transform: translate(-50%, -50%);
    font-size: 46px;
    color: var(--white);
    gap: 14px;
  }
  .card--back .wordmark__square { width: 32px; height: 32px; }
</style>
</head>
<body>
<main class="canvas">
  <section class="card card--front" aria-label="Business card front">
    <div class="wordmark">
      <span class="wordmark__square"></span>
      <span class="wordmark__name">Quorvel</span>
    </div>
    <div class="contact">
      <p class="contact__name">Helen Brackwood</p>
      <p class="contact__role">Director</p>
      <p class="contact__line">+44 (0)1372 904213</p>
      <p class="contact__line">+44 (0)7700 900562</p>
      <p class="contact__line">hbrackwood@quorvel.example</p>
      <p class="contact__line">www.quorvel.example</p>
    </div>
    <div class="address-band">Quorvel Software Limited 42B Millbank Lane, Epsom, Surrey, KT19 3DW</div>
  </section>

  <section class="card card--back" aria-label="Business card back">
    <div class="wordmark">
      <span class="wordmark__square"></span>
      <span class="wordmark__name">Quorvel</span>
    </div>
  </section>
</main>
</body>
</html>
```